Website for AV installation with booking system and e-commerce

Company: Corvexa
Tag Line: Audio Visual and Security System Installations
We need a website for an AV company based in Sydney Australia. We specialise in Audio Visual, CCTV (security cameras), and Data Cabling.
The purpose of the website is that customers book their installation online with a live booking system.
We are looking for the following:
- Creative and modern design
- easy to use - keep in mind that the user who will book will have little knowledge in technology.
- clean and organised
- colours to work in well with our logo we also like royal to navy blue, but we are open to other suggested what works well with our logo.
We want customers to be able to add products needed for their installation ie when booking to wall mount their TV they can choose to add a TV bracket and cables to the cart and vise-versa buy a bracket or cables and add to cart the installation.
Tabs to be included:
About us
Gallery
Contact Us
Home
Services (there are three services that we offer - Residential, Corporate and Retail)
Products
Book Online/Cart (checkout)
Temporary website checkout: www.corvexa.com.au, please note this is very basic and we do not want a copy of this. This is purely to give you an idea of our company.
Good Luck!
Target Market(s)
home owners/renters, business owners, archiects/designers, builders
Industry/Entity Type
E-Commerce
Look and feel

```html
<!DOCTYPE html>
<html lang="en">
<head>
<meta charset="utf-8">
<title>Corvexa – Products – Cables</title>
<link href="https://fonts.googleapis.com/css2?family=Mulish:wght@400;600;700;800&display=swap" rel="stylesheet">
<style>
:root{
  --navy:#0b3461;
  --navy-deep:#062a52;
  --red:#cc0a14;
  --card:#e5e5e5;
  --ink:#111;
  --price:#1d4a7c;
  --white:#fff;
}
*{box-sizing:border-box;margin:0;padding:0}
html,body{width:1200px;height:1000px;overflow:hidden;background:var(--white);font-family:"Mulish",sans-serif}
.page{position:absolute;left:103px;top:92px;width:990px;height:750px;
  box-shadow:-3px 0 4px -2px rgba(40,80,110,.35),3px 0 4px -2px rgba(40,80,110,.35)}
.header{position:absolute;left:0;top:0;width:990px;height:118px;
  background:linear-gradient(100deg,var(--navy-deep) 0%,#0d3e6e 45%,#6f8fae 75%,#c9d6e3 100%);overflow:hidden}
.header .swoosh{position:absolute;left:0;top:0}
.brand{position:absolute;left:18px;top:26px;display:flex;align-items:center;gap:10px;
  color:var(--white);font-weight:800;font-size:48px;letter-spacing:1px}
.brand .mark{width:22px;height:22px;background:var(--red);border-radius:50%}
.tagline{position:absolute;left:353px;top:52px;color:#e9f0f7;font-size:19px;font-variant:small-caps;letter-spacing:1px}
.contact{position:absolute;left:14px;top:101px;color:#dde6ef;font-size:11px;letter-spacing:.3px}
.cart{position:absolute;right:18px;top:92px;color:var(--white);font-size:13px;display:flex;align-items:center;gap:6px;
  text-shadow:0 0 3px rgba(6,42,82,.8)}
.nav{position:absolute;left:0;top:124px;width:160px;list-style:none}
.nav li{height:30px;line-height:30px;padding-left:14px;color:var(--navy);font-weight:700;font-size:17px;letter-spacing:1px;white-space:nowrap}
.nav li .accent{color:var(--red)}
.nav li.sub{padding-left:19px;font-size:15px;font-variant:small-caps;letter-spacing:.8px}
.nav li.active{background:var(--red);color:var(--white);width:74px}
.quote{position:absolute;left:14px;top:404px;width:109px;height:51px;background:var(--navy);border-radius:8px;
  box-shadow:2px 3px 4px rgba(0,0,0,.35);color:var(--white);text-align:center;font-weight:800;line-height:1}
.quote .a{display:block;font-size:14px;padding-top:7px}
.quote .b{display:block;font-size:27px}
h2{position:absolute;left:165px;color:var(--red);font-size:21px;font-variant:small-caps;font-weight:800;letter-spacing:.5px}
.card{position:absolute;width:261px;height:134px;background:var(--card)}
.card .photo{position:absolute;left:4px;top:4px;width:132px;height:125px;
  background:radial-gradient(circle at 50% 55%,#cfcfcf 0%,#f4f4f4 55%,#fff 80%)}
.card .info{position:absolute;left:138px;top:13px;width:121px;text-align:center;font-size:10px;line-height:11.5px;color:var(--ink);letter-spacing:.3px;white-space:nowrap}
.card .price{display:block;color:var(--price);font-weight:800;font-size:9.5px;line-height:11px}
.booking{position:absolute;left:914px;top:861px;width:166px;height:28px;background:var(--red);color:var(--white);
  font-size:18px;font-weight:600;text-align:center;line-height:28px;letter-spacing:.5px}
</style>
</head>
<body>
<div class="page">
  <header class="header">
    <svg class="swoosh" width="990" height="118" viewBox="0 0 990 118" aria-hidden="true">
      <path d="M0 58 Q300 48 620 64 T990 68 L990 72 Q640 80 320 68 T0 72Z" fill="rgba(255,255,255,.18)"/>
    </svg>
    <div class="brand"><span class="mark"></span>Corvexa</div>
    <div class="tagline">Audio Visual And Security System Installations</div>
    <div class="contact">Harbour Lane 18, Sydney, New South Wales 2000, Australia &nbsp;|&nbsp; 00 61 2 5550 1834 &nbsp;|&nbsp; hello@corvexa.com.au</div>
    <div class="cart">
      <svg width="26" height="22" viewBox="0 0 26 22" aria-hidden="true"><path d="M1 2h4l3 12h13l3-9H7" fill="none" stroke="#ffffff" stroke-width="2"/><circle cx="10" cy="18" r="2" fill="#ffffff"/><circle cx="19" cy="18" r="2" fill="#ffffff"/></svg>
      Shopping Cart (3)
    </div>
  </header>

  <ul class="nav">
    <li>HOME</li>
    <li>ABOUT US</li>
    <li>GALLERY</li>
    <li>SERVICES <span class="accent">▾</span></li>
    <li>PRODUCTS <span class="accent">...</span></li>
    <li class="sub active">Cables</li>
    <li class="sub">TV Brackets</li>
    <li class="sub">Security Cameras</li>
    <li>CONTACT US</li>
  </ul>
  <div class="quote"><span class="a">REQUEST A</span><span class="b">QUOTE</span></div>

  <h2 style="top:124px">Products &gt; Cables</h2>

  <div class="card" style="left:165px;top:156px"><div class="photo" role="img" aria-label="Photo of black RCA cable"></div><div class="info">CRX-512-M(KT-3307)<br>1.5M 3RCA M-F Cable<span class="price">$1.50</span></div></div>
  <div class="card" style="left:433px;top:156px"><div class="photo" role="img" aria-label="Photo of green flat USB cable"></div><div class="info">VLX-618-M (KT-2051)<br>1M Flat Cord USB to<br>Phone 8-Pin Cable<span class="price">$2.50</span></div></div>
  <div class="card" style="left:705px;top:156px"><div class="photo" role="img" aria-label="Photo of red USB cable"></div><div class="info">CRX-407-X (KZ-4826)<br>1M USB Phone<br>8-Pin Cable<span class="price">$1.99</span></div></div>

  <div class="card" style="left:165px;top:295px"><div class="photo" role="img" aria-label="Photo of black VGA cable"></div><div class="info">CRX-512-M(KT-3307)<br>1.5M 3RCA M-F Cable<span class="price">$1.50</span></div></div>
  <div class="card" style="left:433px;top:295px"><div class="photo" role="img" aria-label="Photo of component video cable"></div><div class="info">VLX-618-M (KT-2051)<br>1M Flat Cord USB to<br>Phone 8-Pin Cable<span class="price">$2.50</span></div></div>
  <div class="card" style="left:705px;top:295px"><div class="photo" role="img" aria-label="Photo of grey network cable"></div><div class="info">CRX-407-X (KZ-4826)<br>1M USB Phone<br>8-Pin Cable<span class="price">$1.99</span></div></div>

  <div class="card" style="left:165px;top:434px"><div class="photo" role="img" aria-label="Photo of USB power cable"></div><div class="info">CRX-512-M(KT-3307)<br>1.5M 3RCA M-F Cable<span class="price">$1.50</span></div></div>
  <div class="card" style="left:433px;top:434px"><div class="photo" role="img" aria-label="Photo of USB adapter cable"></div><div class="info">VLX-618-M (KT-2051)<br>1M Flat Cord USB to<br>Phone 8-Pin Cable<span class="price">$2.50</span></div></div>
  <div class="card" style="left:705px;top:434px"><div class="photo" role="img" aria-label="Photo of network cable spool"></div><div class="info">CRX-407-X (KZ-4826)<br>1M USB Phone<br>8-Pin Cable<span class="price">$1.99</span></div></div>

  <h2 style="top:600px">Recommended for you:</h2>
  <div class="card" style="left:165px;top:632px"><div class="photo" style="width:120px;top:7px;height:120px" role="img" aria-label="Photo of black HDMI cable"></div><div class="info">CRX-512-M(KT-3307)<br>1.5M 3RCA M-F Cable<span class="price">$1.50</span></div></div>
</div>
<div class="booking">LIVE BOOKING</div>
</body>
</html>
```